Business Card Design - Crisp & Clean

Looking for a new clean and crisp business card design. Design must incorporate our corporate colors (see attached style sheet). We're a pretty fun loving group who likes to keep it light while still portraying a professional image. Card should incorporate both our logo and our mascot (see attachment). Card should be double sided and should have room for our social media - Gleamrow, Brisk Hub and Zumbly on the back. Font selections do not have to match the style guide.

```html
<!DOCTYPE html>
<html lang="en">
<head>
<meta charset="utf-8">
<title>LumenPeople Business Card</title>
<link href="https://fonts.googleapis.com/css2?family=Open+Sans:ital,wght@0,400;0,600;0,700;1,700&family=Oswald:wght@600&display=swap" rel="stylesheet">
<style>
  :root {
    --page: #ecebe8;
    --card: #ffffff;
    --charcoal: #4a4b4d;
    --sun: #fcc22e;
    --sun-soft: #ffe08a;
    --ink: #111111;
    --accent: #f15a22;
    --paper-text: #ffffff;
  }
  html, body {
    margin: 0;
    width: 1200px;
    height: 854px;
    overflow: hidden;
    background: var(--page);
    font-family: "Open Sans", Arial, sans-serif;
  }
  .sheet {
    position: relative;
    width: 1200px;
    height: 854px;
  }
  .card {
    position: absolute;
    left: 260px;
    width: 680px;
    height: 388px;
    background: var(--card);
    box-shadow: 0 6px 18px rgba(0,0,0,0.18);
    overflow: hidden;
  }
  .card--back { top: 24px; }
  .card--front { top: 442px; }
  .card svg.bands {
    position: absolute;
    inset: 0;
  }
  .brand {
    position: absolute;
    display: flex;
    align-items: center;
    gap: 12px;
    font-weight: 700;
    color: var(--ink);
    white-space: nowrap;
  }
  .mascot {
    display: block;
    border-radius: 8px;
    background: linear-gradient(160deg, var(--sun-soft), var(--sun));
  }
  .card--back .brand { left: 150px; top: 86px; font-size: 46px; }
  .card--back .mascot { width: 58px; height: 58px; }
  .card--front .brand { left: 30px; top: 184px; font-size: 22px; }
  .card--front .mascot { width: 34px; height: 34px; border-radius: 5px; }
  .back-tagline {
    position: absolute;
    left: 352px;
    top: 210px;
    margin: 0;
    font-size: 20px;
    font-style: italic;
    font-weight: 700;
    color: var(--sun);
    white-space: nowrap;
  }
  .socials {
    position: absolute;
    left: 40px;
    top: 300px;
    margin: 0;
    padding: 0;
    list-style: none;
    display: flex;
    gap: 34px;
    font-size: 16px;
    font-weight: 600;
    color: var(--paper-text);
  }
  .socials__item {
    display: flex;
    align-items: center;
    gap: 8px;
  }
  .socials__item::before {
    content: "";
    width: 12px;
    height: 12px;
    border-radius: 50%;
    background: var(--sun);
  }
  .person-name {
    position: absolute;
    left: 28px;
    top: 26px;
    margin: 0;
    font-family: "Oswald", Impact, sans-serif;
    font-weight: 600;
    font-size: 38px;
    letter-spacing: 0.5px;
    color: var(--sun);
  }
  .person-role {
    position: absolute;
    right: 26px;
    top: 61px;
    margin: 0;
    font-size: 17px;
    font-weight: 700;
    color: var(--ink);
  }
  .contact {
    position: absolute;
    left: 262px;
    top: 168px;
    margin: 0;
    font-size: 21px;
    line-height: 1.45;
    color: var(--ink);
    white-space: nowrap;
  }
  .contact__company { font-weight: 600; }
  .contact__mobile { color: var(--accent); }
</style>
</head>
<body>
<main class="sheet">
  <section class="card card--back" aria-label="Card back">
    <svg class="bands" width="680" height="388" viewBox="0 0 680 388" aria-hidden="true">
      <path d="M360,186 H680 V200 H372 C366,196 364,190 360,186 Z" fill="var(--sun)"/>
      <path d="M0,388 V262 H300 C335,262 340,200 380,200 H680 V388 Z" fill="var(--charcoal)"/>
      <rect x="0" y="360" width="680" height="6" fill="var(--sun)"/>
    </svg>
    <div class="brand"><span class="mascot" role="img" aria-label="Lightbulb mascot"></span>LumenPeople</div>
    <p class="back-tagline">LumenPeople Processing Solution</p>
    <ul class="socials" aria-label="Social media">
      <li class="socials__item">Gleamrow</li>
      <li class="socials__item">Brisk Hub</li>
      <li class="socials__item">Zumbly</li>
    </ul>
  </section>

  <section class="card card--front" aria-label="Card front">
    <svg class="bands" width="680" height="388" viewBox="0 0 680 388" aria-hidden="true">
      <path d="M0,0 H680 V50 H430 C400,50 395,96 360,96 H0 Z" fill="var(--charcoal)"/>
      <path d="M418,58 H680 V94 H386 C405,94 402,58 418,58 Z" fill="var(--sun)"/>
      <rect x="0" y="334" width="680" height="8" fill="var(--sun)"/>
      <rect x="0" y="342" width="680" height="46" fill="var(--charcoal)"/>
    </svg>
    <h1 class="person-name">MARA ELLISON</h1>
    <p class="person-role">Marketing Wizard</p>
    <div class="brand"><span class="mascot" role="img" aria-label="Lightbulb mascot"></span>LumenPeople</div>
    <p class="contact">
      <span class="contact__company">LumenPeople Processing Solution</span><br>
      mara@lumenpeople.com<br>
      <span class="contact__mobile">Mobile: 555-014-2290</span>
    </p>
  </section>
</main>
</body>
</html>
```